IG ad to attract older men for better health #1

I want a bold headline Instagram Ad that coordinate with my website design with a racy sexy woman to attract men 45yrs old plus. See Two samples attached

Target Market(s)

Men 45 years old and older

Industry/Entity Type

Health And Wellness

Requirements
Must have
• eye catching appeal to men
Nice to have
• The copy to read
Kestrel61go is the headline at the top of the page. Then the copy reads...
"I want to seduce you to better health with a little T&A. Remove the excuses, provide ridiculously simple tips and advice to get you started on a path of lasting heath." Want more?

```html
<!DOCTYPE html>
<html lang="en">
<head>
<meta charset="utf-8">
<title>Kestrel61go – Better Health Ad</title>
<link rel="stylesheet" href="https://fonts.googleapis.com/css2?family=Bebas+Neue&family=Poppins:wght@500&display=swap">
<style>
  :root {
    --red: #d42a30;
    --deep-red: #5a0d14;
    --black: #0b0b0d;
    --yellow: #f8f51f;
    --white: #ffffff;
    --cta-start: #4a0610;
    --cta-mid: #f0262c;
    --cta-end: #ffe526;
    --skin: #b57a5c;
    --hair: #3a2418;
  }
  * { margin: 0; padding: 0; box-sizing: border-box; }
  html, body { width: 1200px; height: 992px; overflow: hidden; background: var(--black); }
  .ad {
    position: relative;
    width: 1200px;
    height: 992px;
    overflow: hidden;
    background: linear-gradient(90deg, var(--red) 0%, #b0222a 22%, var(--deep-red) 45%, #1c1114 62%, var(--black) 85%);
  }
  .model-photo {
    position: absolute;
    left: 20px;
    top: 50px;
    width: 670px;
    height: 942px;
    border-radius: 46% 46% 8% 8% / 30% 30% 4% 4%;
    background:
      radial-gradient(ellipse 30% 22% at 50% 30%, var(--skin) 0%, rgba(181,122,92,0) 100%),
      radial-gradient(ellipse 48% 28% at 50% 72%, #d23a2e 0%, rgba(210,58,46,0) 100%),
      linear-gradient(180deg, var(--hair) 0%, #5b3a2a 45%, #8a3a2c 100%);
    opacity: 0.85;
  }
  .copy {
    position: absolute;
    right: 58px;
    top: 0;
    width: 560px;
    height: 760px;
    text-align: right;
  }
  .brand-name {
    position: absolute;
    right: 0;
    top: 140px;
    font-family: "Poppins", sans-serif;
    font-weight: 500;
    font-size: 64px;
    line-height: 96px;
    color: var(--yellow);
    white-space: nowrap;
  }
  .headline {
    position: absolute;
    right: 18px;
    top: 298px;
    font-family: "Bebas Neue", sans-serif;
    font-weight: 400;
    font-size: 50px;
    line-height: 56px;
    letter-spacing: 1px;
    color: var(--white);
    white-space: nowrap;
  }
  .body-copy {
    position: absolute;
    right: 0;
    top: 500px;
    font-family: "Poppins", sans-serif;
    font-weight: 500;
    font-size: 33px;
    line-height: 50px;
    letter-spacing: 1px;
    color: var(--yellow);
    white-space: nowrap;
  }
  .cta {
    position: absolute;
    left: 678px;
    top: 794px;
    width: 464px;
    height: 114px;
    border-radius: 0 57px 57px 0;
    background: linear-gradient(90deg, var(--cta-start) 0%, #8e0f18 25%, var(--cta-mid) 55%, #f86a2a 78%, var(--cta-end) 100%);
    font-family: "Bebas Neue", sans-serif;
    font-size: 72px;
    line-height: 114px;
    letter-spacing: 1px;
    color: var(--white);
    text-align: right;
    padding-right: 62px;
    text-decoration: none;
  }
</style>
</head>
<body>
  <main class="ad">
    <div class="model-photo" role="img" aria-label="Smiling woman with long brunette hair wearing a red bra and gold heart necklace"></div>
    <section class="copy">
      <h1 class="brand-name">Kestrel61go</h1>
      <h2 class="headline">I want to seduce you<br>to better health<br>with a little T&amp;A.</h2>
      <p class="body-copy">Remove the excuses,<br>provide ridiculously<br>simple tips and advice to<br>get you started on a path<br>of lasting health</p>
    </section>
    <a class="cta" href="#">Want more?</a>
  </main>
</body>
</html>
```